Business Card Design Project

We consult with hotels on setting rates and maximizing a revenue strategy

Industry/Entity Type

Business

Contact Information for Business Card

I am not sure what I want. Our company offers high level consulting to hotels around the country but we are also laid back. I would like something that is professional but also shows the laid back side

```html
<!DOCTYPE html>
<html lang="en">
<head>
<meta charset="utf-8">
<title>Harborline Business Card</title>
<link href="https://fonts.googleapis.com/css2?family=Open+Sans:wght@400;700&display=swap" rel="stylesheet">
<style>
  :root {
    --stage: #4e5d6c;
    --green: #1f7e5f;
    --green-light: #5bb99a;
    --ink: #201814;
    --paper: #ffffff;
    --label: #ffffff;
  }
  * { box-sizing: border-box; margin: 0; padding: 0; }
  html, body { width: 1000px; height: 1200px; overflow: hidden; }
  body {
    background: var(--stage);
    font-family: "Open Sans", sans-serif;
    position: relative;
  }
  .side-label {
    position: absolute;
    color: var(--label);
    font-size: 42px;
    font-weight: 400;
    letter-spacing: 1px;
  }
  .side-label--front { left: 205px; top: 150px; }
  .side-label--back { left: 810px; top: 890px; }
  .card {
    position: absolute;
    width: 590px;
    height: 336px;
    background: var(--paper);
    overflow: hidden;
    box-shadow: 0 18px 40px rgba(20, 28, 38, 0.45);
  }
  .card--front { left: 205px; top: 215px; }
  .card--back { left: 205px; top: 545px; }
  .card__art { position: absolute; inset: 0; width: 100%; height: 100%; }
  .brand {
    position: absolute;
    display: flex;
    align-items: center;
    gap: 12px;
    color: var(--ink);
    font-weight: 700;
  }
  .brand__mark { background: var(--green); display: block; }
  .card--front .brand { left: 0; right: 0; top: 140px; justify-content: center; font-size: 38px; }
  .card--front .brand__mark { width: 34px; height: 34px; }
  .card--back .brand { left: 38px; top: 70px; font-size: 22px; }
  .card--back .brand__mark { width: 20px; height: 20px; }
  .contact { position: absolute; left: 54px; top: 172px; color: var(--paper); }
  .contact__name { font-size: 22px; font-weight: 700; margin-left: 4px; margin-bottom: 12px; }
  .contact__line { font-size: 19px; font-weight: 400; line-height: 34px; white-space: nowrap; }
  .contact__line span + span { margin-left: 16px; }
  .website {
    position: absolute;
    right: 20px;
    bottom: 22px;
    color: var(--paper);
    font-size: 15px;
  }
</style>
</head>
<body>
  <div class="side-label side-label--front">FRONT</div>

  <section class="card card--front">
    <svg class="card__art" viewBox="0 0 590 336" aria-hidden="true">
      <path d="M0 0 H105 C135 110 130 230 90 336 H0 Z" fill="var(--green)"/>
      <path d="M0 0 H80 C108 110 104 230 66 336 H0 Z" fill="var(--green-light)"/>
      <circle cx="650" cy="440" r="250" fill="var(--green)"/>
      <circle cx="675" cy="465" r="215" fill="var(--green-light)"/>
    </svg>
    <div class="brand"><span class="brand__mark"></span>Harborline</div>
  </section>

  <section class="card card--back">
    <svg class="card__art" viewBox="0 0 590 336" aria-hidden="true">
      <rect width="590" height="336" fill="var(--green)"/>
      <path d="M0 0 H590 C530 100 320 170 0 160 Z" fill="var(--ink)"/>
      <path d="M0 0 H590 C520 110 300 150 0 135 Z" fill="var(--paper)"/>
    </svg>
    <div class="brand"><span class="brand__mark"></span>Harborline</div>
    <div class="contact">
      <p class="contact__name">Dana Whitfield</p>
      <p class="contact__line"><span>Regional Revenue Manager</span><span>Office 555 014 2287</span></p>
      <p class="contact__line"><span>Fax 555 014 3391</span><span>dana@harborlinerm.com</span></p>
    </div>
    <p class="website">www.harborlinerm.com</p>
  </section>

  <div class="side-label side-label--back">BACK</div>
</body>
</html>
```